Brochure, website and corporate stationary Design Project

Project scope:
1 x brochure (A4 insert) design
1 x brochure folder design (both external pages and one internal (there will be a few lines of text on the left inside page). The internal right side page will be a pocket for brochures (A4 inserts)
1 x corporate stationary pack (Business Card, logo (a proper logo file format needs to be produced), Letterhead and Envelope)
1 x concept design for our website. You dont need to do the coding. What you need to deliver is the design in a standard format (i.e. photoshop or blend)
Summary: the scope of the project is to design our brochure and its brochure folder, corporate stationary design and graphics concept design for our website. You should also consider our existing logo when performing the above design work (you can modify the logo slightly if you think it would improve look and feel and relevancy to overall design).
• We are a small IT services company
• The folder will be used to hold the brochures (inserts). The folder will be given to prospect customers (see attached a sample service brochure called “Fjällux User support services Ver0.1.docx”)
• On the cover of the folder, we want to have a design that uses keywords / phrases that reflects our main services (see attached file called “Phrases for presentation folder.docs”). Please note that not all phrases have to be used, use a logic in which ones or add new suggestions
• Inside the folder, at left side we want to have a short text explaining about our services a bit (see attached file called “Brochure Main section v0.91.docx”)
• All designs (corporate stationary, brochure, folder, web, etc.) must be consistent with each other and follow same concept, colour scheme, etc
• you are allowed to do minor changes to our existing logo if you have good reason to do so (see attached logo)
• We want our website design to be simple, elegant, not very colourful, light. HTML5. No flash. (you dont need to do the actual coding of the website, just deliver the design in Photoshop, Blend or any other standard format) With minimal menu items such as: home, services, about us, news, contact us, and other important ones if any. Same colour and design scheme as corporate stationary and brochures
• The company name “Fjällux” is derived from the Swedish word “Grön” (meaning green) and “teQ” which stands for technology but spelled with a “Q” to resemble Quality. The corporate green colour comes from the word “Grön”.
• All templates must be delivered in a standard editable format
Reason: To provide more time to the designers to come with their design submissions.
please note that we more than doubled the budget for this project
We deliver IT services to companies of 3-4 employees upto 200-300 employees. The brochures are intended for prospect customers (non IT people)
Business

```html
<!DOCTYPE html>
<html lang="en">
<head>
<meta charset="utf-8">
<title>Fjällux – brand development</title>
<link rel="stylesheet" href="https://fonts.googleapis.com/css2?family=Montserrat:wght@800&family=Open+Sans:wght@400;600;700&family=Nothing+You+Could+Do&display=swap">
<style>
:root{
  --board:#ececec;
  --paper:#ffffff;
  --green-dark:#0b6326;
  --green:#1b8a3a;
  --lime:#8cc63f;
  --ink:#4a4a4a;
  --ink-soft:#8a8a8a;
  --label:#2b2b2b;
  --photo-a:#e4e9ef;
  --photo-b:#c8b29c;
}
*{box-sizing:border-box;margin:0;padding:0}
html,body{width:1200px;height:1020px;overflow:hidden;background:var(--board)}
body{position:relative;font-family:"Open Sans",Arial,sans-serif;color:var(--ink)}
.board-title{position:absolute;left:840px;top:14px;font-family:"Nothing You Could Do",cursive;font-size:46px;color:#222;letter-spacing:1px}
.label{position:absolute;font-family:"Nothing You Could Do",cursive;font-size:14px;color:var(--label);white-space:nowrap}
.piece{position:absolute;background:var(--paper);box-shadow:0 1px 3px rgba(0,0,0,.25);overflow:hidden}
.piece > svg.shapes{position:absolute;left:0;top:0;width:100%;height:100%}
.logo{position:absolute;font-family:"Montserrat",Arial,sans-serif;font-weight:800;color:var(--ink);letter-spacing:.02em;white-space:nowrap;display:flex;align-items:center}
.logo .dot{display:inline-block;border-radius:50%;background:var(--lime);margin-left:.15em}
.tiny{position:absolute;font-size:3.6px;line-height:5.4px;color:#555}
.tiny p{margin-bottom:4px}
.photo{position:absolute}

/* new brand */
.tagline{position:absolute;left:200px;top:270px;width:114px;text-align:right;font-family:"Nothing You Could Do",cursive;font-size:14px;line-height:16px;color:var(--ink)}
.tagline em{font-style:normal;color:var(--lime)}

/* website */
.web-nav{position:absolute;left:6px;font-size:4.2px;letter-spacing:.08em;color:var(--ink-soft)}
.web-nav b{color:var(--green);font-weight:600}
.web-foot{position:absolute;left:0;bottom:0;width:100%;height:18px;background:var(--green-dark);color:#fff;font-size:3.6px;display:flex;align-items:center;justify-content:space-between;padding:0 6px}
.web-foot .slogan{font-size:7px;font-style:italic;font-weight:600}
.web-foot .slogan em{color:var(--lime)}
.web-side{position:absolute;background:var(--green-dark);color:#fff;font-size:3.6px;line-height:5px;padding:5px}
.web-side h4{color:var(--lime);font-size:4px;font-weight:600;margin-bottom:3px;line-height:5px}
.login{position:absolute;border-top:1px solid #ccc;font-size:3.4px;color:#888}
.login span{display:block;height:5px;border:1px solid #ddd;margin-top:2px}

/* folder interior */
.intro{position:absolute;left:14px;top:96px;width:236px;font-size:4.6px;line-height:6.6px;color:#555}
.intro p{margin-bottom:4px}
.intro h3{color:var(--lime);font-size:6px;font-weight:400;margin:6px 0 3px}
.process{display:flex;margin:5px 0 6px}
.process span{background:var(--green);color:#fff;font-size:4.4px;padding:2px 7px 2px 4px;margin-right:1px;clip-path:polygon(0 0,88% 0,100% 50%,88% 100%,0 100%)}
.intro ol{list-style:none}
.intro ol li::before{content:"› ";color:var(--lime)}
</style>
</head>
<body>

<h1 class="board-title">brand development</h1>

<!-- NEW BRAND -->
<div class="label" style="left:50px;top:114px">new brand</div>
<div class="piece" style="left:50px;top:136px;width:263px;height:133px">
  <div class="logo" style="left:32px;top:44px;font-size:38px">Fjällux<span class="dot" style="width:14px;height:14px"></span></div>
</div>
<div class="tagline"><em>more</em> powerful<br><em>more</em> strong<br><em>more</em> balanced</div>

<!-- BUSINESS CARD -->
<div class="piece" style="left:50px;top:374px;width:95px;height:66px">
  <svg class="shapes" viewBox="0 0 95 66" preserveAspectRatio="none">
    <path d="M0,58 Q50,52 95,56 L95,66 L0,66Z" fill="var(--lime)"/>
    <path d="M0,62 Q50,57 95,61 L95,66 L0,66Z" fill="var(--green-dark)"/>
  </svg>
  <div class="tiny" style="left:4px;top:4px;font-size:2.6px;line-height:3.6px">
    <b style="color:var(--green)">Anna Lind</b><br>Support Manager<br><br>T +000 4 555 0100<br>M +000 50 555 0199<br>anna@fjallux.example<br>www.fjallux.example<br>PO Box 1200, Dubai, UAE
  </div>
  <div class="logo" style="left:47px;top:5px;font-size:9px">Fjällux<span class="dot" style="width:3px;height:3px"></span></div>
</div>
<div class="label" style="left:156px;top:414px">business card</div>

<!-- ENVELOPE -->
<div class="label" style="left:264px;top:447px">envelope</div>
<div class="piece" style="left:50px;top:470px;width:263px;height:133px">
  <svg class="shapes" viewBox="0 0 263 133" preserveAspectRatio="none">
    <path d="M0,0 L263,0 L263,10 Q150,4 0,12Z" fill="var(--green-dark)"/>
    <path d="M0,12 Q150,4 263,10 L263,14 Q150,7 0,15Z" fill="var(--lime)"/>
    <path d="M0,110 Q100,118 263,122 L263,133 L0,133Z" fill="var(--lime)"/>
    <path d="M0,118 Q120,124 263,126 L263,133 L0,133Z" fill="var(--green-dark)"/>
  </svg>
  <div class="logo" style="left:6px;top:19px;font-size:11px">Fjällux<span class="dot" style="width:3px;height:3px"></span></div>
  <div class="tiny" style="left:7px;top:37px;font-size:2.8px;line-height:3.8px">PO Box 1200<br>Dubai, UAE</div>
</div>

<!-- LETTERHEAD -->
<div class="label" style="left:250px;top:608px">letterhead</div>
<div class="piece" style="left:50px;top:632px;width:255px;height:337px">
  <svg class="shapes" viewBox="0 0 255 337" preserveAspectRatio="none">
    <path d="M0,0 L255,0 L255,12 Q150,4 0,10Z" fill="var(--green-dark)"/>
    <path d="M40,10 Q150,3 255,12 L255,16 Q150,7 40,10Z" fill="var(--lime)"/>
    <path d="M0,306 Q120,300 255,312 L255,337 L0,337Z" fill="var(--lime)"/>
    <path d="M0,312 Q130,308 255,318 L255,337 L0,337Z" fill="var(--green-dark)"/>
  </svg>
  <div class="logo" style="left:188px;top:18px;font-size:12px">Fjällux<span class="dot" style="width:3px;height:3px"></span></div>
  <div class="tiny" style="left:18px;top:58px;width:220px">
    <p>Dear Client,</p>
    <p>Thank you for your interest in our services. We help small and growing firms plan, build and support the systems they rely on every day.</p>
    <p>Our team works as a trusted adviser, keeping your network, email and desktops running so your staff can focus on the work that matters.</p>
    <p>Please find enclosed our service brochure. We would be glad to arrange a short meeting to discuss your needs and how we can help.</p>
    <p>Thank you for your interest in our services. We help small and growing firms plan, build and support the systems they rely on every day.</p>
    <p>Our team works as a trusted adviser, keeping your network, email and desktops running so your staff can focus on the work that matters.</p>
    <p>Please find enclosed our service brochure. We would be glad to arrange a short meeting to discuss your needs and how we can help.</p>
  </div>
  <div class="tiny" style="left:196px;top:250px;text-align:right">Kind regards,<br><br>Elin Varga</div>
  <svg style="position:absolute;left:205px;top:266px" width="30" height="8" viewBox="0 0 30 8"><path d="M1,6 Q6,0 9,5 T18,4 L28,5" fill="none" stroke="#333" stroke-width=".6"/></svg>
  <div class="tiny" style="left:14px;top:324px;color:#fff;font-size:2.8px">PO Box 1200 | T +000 4 555 0100 | info@fjallux.example | www.fjallux.example</div>
</div>

<!-- BROCHURE -->
<div class="label" style="left:548px;top:20px">brochure</div>
<div class="piece" style="left:346px;top:41px;width:251px;height:357px">
  <div class="photo" role="img" aria-label="Photo of a smiling businesswoman in front of blurred colleagues" style="left:0;top:0;width:251px;height:250px;background:radial-gradient(circle at 55% 35%,var(--photo-b) 0 18%,transparent 40%),linear-gradient(180deg,#f1f3f6,var(--photo-a) 60%,#b9c6d6)"></div>
  <svg class="shapes" viewBox="0 0 251 357" preserveAspectRatio="none">
    <path d="M0,248 Q120,252 251,222 L251,252 L0,252Z" fill="var(--green-dark)"/>
    <path d="M0,252 L0,238 Q130,246 251,224 L251,236 Q130,255 0,250Z" fill="var(--lime)"/>
    <path d="M0,250 Q130,256 251,236 L251,262 L0,262Z" fill="#fff"/>
    <path d="M0,318 Q150,312 251,322 L251,357 L0,357Z" fill="var(--lime)"/>
    <path d="M0,328 Q150,322 251,334 L251,357 L0,357Z" fill="var(--green-dark)"/>
  </svg>
  <div class="logo" style="left:122px;top:288px;font-size:22px">Fjällux<span class="dot" style="width:6px;height:6px"></span></div>
  <div style="position:absolute;left:152px;top:320px;font-size:4px;letter-spacing:.18em;font-weight:600">USER SUPPORT SERVICES</div>
</div>

<!-- WEBSITE HOME -->
<div class="label" style="left:556px;top:410px">website</div>
<div class="piece" style="left:346px;top:432px;width:251px;height:271px">
  <svg class="shapes" viewBox="0 0 251 271" preserveAspectRatio="none">
    <path d="M80,0 L251,0 L251,22 Q170,10 80,0Z" fill="var(--green-dark)"/>
    <path d="M80,0 Q170,10 251,22 L251,26 Q160,12 80,0Z" fill="var(--lime)"/>
  </svg>
  <div class="logo" style="left:6px;top:18px;font-size:13px">Fjällux<span class="dot" style="width:3px;height:3px"></span></div>
  <div class="tiny" style="left:6px;top:36px;width:120px;color:var(--lime);font-size:3.2px;line-height:4.4px">IT services that keep small and medium businesses running smoothly, securely and ready to grow.</div>
  <div class="login" style="left:180px;top:28px;width:64px">LOGIN<span></span><span></span></div>
  <div class="login" style="left:180px;top:55px;width:64px">SEARCH<span></span></div>
  <div class="web-nav" style="top:62px">HOME &nbsp;|&nbsp; SERVICES &nbsp;|&nbsp; ABOUT US &nbsp;|&nbsp; NEWS &nbsp;|&nbsp; CONTACT US</div>
  <div class="photo" role="img" aria-label="Photo of hands holding a small green globe" style="left:6px;top:74px;width:174px;height:88px;background:radial-gradient(circle at 50% 50%,#6f8f3a 0 14%,#c9a27b 24%,#efe4d6 60%,#f6f1ea)"></div>
  <div class="web-side" style="left:180px;top:74px;width:65px;height:88px">
    <h4>MOST POPULAR SERVICES</h4>User support, cloud email and network care for teams of every size.<br><br><span style="color:var(--lime)">READ MORE</span>
  </div>
  <div class="tiny" style="left:6px;top:176px;width:50px;font-size:3px;line-height:4.4px"><b style="color:var(--green)">Latest news</b><br>New cloud backup plans now available for small offices.</div>
  <div class="tiny" style="left:58px;top:170px;width:1px;height:40px;background:#ddd"></div>
  <div class="tiny" style="left:112px;top:172px;width:60px;font-size:3px;line-height:4.4px"><b style="color:var(--green);font-size:3.6px">TESTIMONIAL</b><br>They fixed our network in a day and have supported us ever since.</div>
  <div class="tiny" style="left:186px;top:176px;width:58px;font-size:3px;line-height:4.4px"><b style="color:var(--green)">Contact</b><br>T +000 4 555 0100<br>info@fjallux.example</div>
  <div class="web-foot"><span>Follow us &nbsp; | &nbsp;Newsletter &nbsp; | &nbsp;Privacy policy</span><span class="slogan">Grow <em>your</em> business <em>with us!</em></span></div>
</div>

<!-- WEBSITE ABOUT -->
<div class="label" style="left:556px;top:690px">website</div>
<div class="piece" style="left:346px;top:719px;width:251px;height:251px">
  <svg class="shapes" viewBox="0 0 251 251" preserveAspectRatio="none">
    <path d="M80,0 L251,0 L251,22 Q170,10 80,0Z" fill="var(--green-dark)"/>
    <path d="M80,0 Q170,10 251,22 L251,26 Q160,12 80,0Z" fill="var(--lime)"/>
  </svg>
  <div class="logo" style="left:6px;top:18px;font-size:13px">Fjällux<span class="dot" style="width:3px;height:3px"></span></div>
  <div class="tiny" style="left:6px;top:36px;width:120px;color:var(--lime);font-size:3.2px;line-height:4.4px">IT services that keep small and medium businesses running smoothly, securely and ready to grow.</div>
  <div class="login" style="left:180px;top:28px;width:64px">LOGIN<span></span><span></span></div>
  <div class="login" style="left:180px;top:55px;width:64px">SEARCH<span></span></div>
  <div class="web-nav" style="top:62px">HOME &nbsp;|&nbsp; SERVICES &nbsp;|&nbsp; <b>ABOUT US</b> &nbsp;|&nbsp; NEWS &nbsp;|&nbsp; CONTACT US</div>
  <div class="photo" role="img" aria-label="Photo of a businessman in an office with colleagues behind him" style="left:6px;top:74px;width:174px;height:82px;background:linear-gradient(90deg,#e8ecef,#cfd6dc 50%,#9aa6b0 70%,#dfe3e6)"></div>
  <div class="web-side" style="left:180px;top:74px;width:65px;height:82px">
    <h4>EXPERIENCED PARTNERS IN IT MANAGEMENT</h4><b>SERVICE STATEMENT</b>
  </div>
  <div class="tiny" style="left:6px;top:162px;width:150px;font-size:3px;line-height:4.4px"><b style="color:var(--ink)">Mission statement</b><br>We deliver dependable IT support so that our clients can spend their time on customers, not computers.</div>
  <div class="tiny" style="left:186px;top:166px;width:58px;font-size:3px;line-height:4.4px"><b style="color:var(--green)">Quick links</b><br>Services<br>Careers<br>Support</div>
  <div class="web-foot"><span>Follow us &nbsp; | &nbsp;Newsletter &nbsp; | &nbsp;Privacy policy</span><span class="slogan">Grow <em>your</em> business <em>with us!</em></span></div>
</div>

<!-- FOLDER EXTERIOR -->
<div class="label" style="left:628px;top:155px">folder (exterior)</div>
<div class="piece" style="left:631px;top:180px;width:532px;height:365px">
  <svg class="shapes" viewBox="0 0 532 365" preserveAspectRatio="none">
    <rect x="0" y="0" width="266" height="365" fill="var(--green-dark)"/>
    <line x1="262" y1="0" x2="262" y2="365" stroke="#fff" stroke-width=".6" stroke-dasharray="2 2"/>
    <path d="M266,215 Q400,206 532,190 L532,220 Q400,228 266,232Z" fill="var(--lime)"/>
    <path d="M266,232 Q400,228 532,220 L532,345 Q400,330 266,330Z" fill="var(--green-dark)"/>
    <path d="M266,320 Q400,316 532,326 L532,333 Q400,324 266,328Z" fill="var(--lime)" opacity=".7"/>
    <path d="M266,338 Q400,322 532,348 L532,365 L266,365Z" fill="#fff"/>
  </svg>
  <div class="piece" style="left:0;top:238px;width:86px;height:127px;box-shadow:1px 0 3px rgba(0,0,0,.3)">
    <div class="logo" style="left:24px;top:8px;font-size:10px">Fjällux<span class="dot" style="width:3px;height:3px"></span></div>
    <div class="tiny" style="left:24px;top:24px;font-size:2.6px;line-height:3.6px">
      <b style="color:var(--green)">VISIT ADDRESS</b><br>Building 4, Office 210<br>Dubai, UAE<br>
      <b style="color:var(--green)">MAIL ADDRESS</b><br>PO Box 1200<br>
      <b style="color:var(--green)">PHONE</b> +000 4 555 0100<br>
      <b style="color:var(--green)">WEB</b> www.fjallux.example
    </div>
  </div>
  <div class="logo" style="left:410px;top:32px;font-size:21px">Fjällux<span class="dot" style="width:6px;height:6px"></span></div>
</div>
<div class="label" style="left:631px;top:540px">back</div>
<div class="label" style="left:1128px;top:540px">front</div>

<!-- FOLDER INTERIOR -->
<div class="label" style="left:628px;top:574px">folder (interior)</div>
<div class="label" style="left:1140px;top:574px">brochure</div>
<svg style="position:absolute;left:1110px;top:588px" width="34" height="24" viewBox="0 0 34 24"><path d="M32,2 L6,20" stroke="#555" stroke-width=".8" fill="none"/></svg>
<div class="piece" style="left:631px;top:604px;width:532px;height:365px">
  <svg class="shapes" viewBox="0 0 532 365" preserveAspectRatio="none">
    <path d="M0,0 L532,0 L532,68 Q300,56 0,62Z" fill="var(--green-dark)"/>
    <path d="M0,62 Q300,56 532,68 L532,74 Q300,62 0,66Z" fill="var(--lime)"/>
    <path d="M0,66 Q300,62 532,74 L532,80 L0,80Z" fill="#fff"/>
    <rect x="266" y="0" width="266" height="365" fill="var(--green-dark)"/>
    <line x1="262" y1="70" x2="262" y2="365" stroke="#999" stroke-width=".6" stroke-dasharray="2 2"/>
    <path d="M0,335 Q200,326 532,340 L532,365 L0,365Z" fill="var(--lime)"/>
    <path d="M0,344 Q200,336 532,352 L532,365 L0,365Z" fill="var(--green-dark)"/>
  </svg>
  <div class="photo" role="img" aria-label="Brochure insert with photo of a smiling businesswoman" style="left:278px;top:16px;width:236px;height:238px;background:radial-gradient(circle at 50% 40%,var(--photo-b) 0 20%,transparent 42%),linear-gradient(180deg,#f1f3f6,var(--photo-a) 60%,#b9c6d6);box-shadow:0 0 3px rgba(0,0,0,.3)"></div>
  <svg class="shapes" viewBox="0 0 532 365" preserveAspectRatio="none">
    <path d="M266,300 L266,220 Q420,232 532,196 L532,310 Q400,300 266,300Z" fill="#fff"/>
    <path d="M266,300 Q400,298 532,310 L532,330 Q400,314 266,318Z" fill="var(--lime)"/>
  </svg>
  <div class="logo" style="left:398px;top:258px;font-size:24px">Fjällux<span class="dot" style="width:7px;height:7px"></span></div>
  <div class="intro">
    <div class="logo" style="position:static;font-size:10px;margin-bottom:5px">Fjällux<span class="dot" style="width:3px;height:3px"></span></div>
    <p>We are a prominent information technology management consultancy headquartered in Dubai, providing services across the GCC region.</p>
    <p>We work in a unique way by partnering with clients and acting as a trusted advisor for their management team.</p>
    <p>We provide business leaders with high-quality, up to date and expert strategic advice to help them make informed decisions about their organisations technology investments.</p>
    <p>We cover the entire lifecycle of IT service delivery.</p>
    <div class="process"><span>Management Consultancy</span><span>Solution Design</span><span>Solution Delivery</span><span>Ongoing Support</span></div>
    <h3>SERVICES</h3>
    <p>Our services include the entire range of technology solutions for small, medium and large businesses.</p>
    <p>We offer strategy and business change advice, systems integration and managed services for infrastructure, applications, cyber security, and development of web and mobile software applications.</p>
    <p>To offer such comprehensive services we have handpicked partners that are the best in their field so that we can build exceptional quality and depth into our services while eliminating the need for clients to deal with multiple vendors.</p>
    <p>These include:</p>
    <ol>
      <li>IT Management and Consultancy</li>
      <li>Server, Telephony and Network Installation and Support</li>
      <li>User Support</li>
      <li>Cloud Services – Email, Storage, Business Applications</li>
      <li>Security</li>
      <li>Business Applications i.e. CRM, ERP, Accounting software</li>
      <li>App Development</li>
    </ol>
  </div>
</div>
<div class="label" style="left:631px;top:962px">left</div>
<div class="label" style="left:1132px;top:962px">right</div>
<div class="label" style="left:1168px;top:870px;transform:rotate(90deg);transform-origin:left top">(lappet)</div>
<svg style="position:absolute;left:1164px;top:818px" width="8" height="150" viewBox="0 0 8 150"><path d="M1,1 H6 V149 H1" stroke="#555" stroke-width=".8" fill="none"/></svg>

</body>
</html>
```